LES ALIMENTS DE ROSSOLI épicerie spécialisée \ specialty grocery store

I want a pamphlet for my business, with a list of all my products and prices including the pictures that go with each category, it needs to be eye catching and welcoming, also I will send you a picture of my logo but it needs to be adjusted, its red as shown but there is no shape to it, it is a red background with white writing as shown. let see your best work. I will send you all the info and will keep sending more as we go along. thanks

these are all mt prices and products by category

PIZZA,CALZONE CONGELÉ:

Pizza Napolitana 9.95
Pizza Americana 12.95
Pizza Canadese 14.95
Pizza Spécial De Rossoli 15.95
Pizza Vegeteriana 10.95
Pizza légumes Mix 13.95
Pizza Campagnola 14.95
Pizza Salsiccia e Rapini 13.50
Pizza Bacon 13.95
Pizza Salsiccia di casa 13.95
Pizza Fruits de Mer 17.95
Calzone pepperoni fromage 6.95
Calzone Salsiccia Rapini 6.95
FOCCACIA ALL’ALIO 8.95
PÂTE À PIZZA 1.95

LASAGNE CONGELÉ:

LASAGNA POMODORO 12.95
LASAGNA ALLA DORA 14.50
LASAGNA SAUCE VIANDE 14.50
LASAGNA GIARDINERA 13.95

Spécialité de la maison De Rossoli :

ARANCINI 11.50
POLPETTE DELLA NONNA 11.95
MELANZANE ALLA PARMIGIANA 15.95
PEPPERONI RIPIENI DI MAMMA LUCIA 7.95
CANNELLONI AL FORNO 15.95
MANNICOTTI ALLA FIORENTINA 15.95
POLENTA SALSICIA 15.95
TRIPPA 13.95
PATE CHINOIS 16.95

SAUCES MAISON CONGELÉS ET RÉFRIGÉRÉ:

1L SAUICE VIANDE (RÉFRIGÉRÉ) 13.95
1L SAUCE NAPOLETANA (RÉFRIGÉRÉ) 10.50

500ML SAUCE VIANDE CONGELÉ 6.25
500ML SAUCE LINA CONGELÉ 7.95
500ML SAUCE SERENA CONGELÉ (SAUCE ROSÉE) 6.95
500ML SAUCE ARRABIATA CONGELÉ 6.95

POISSONS, FRUITS DE MER ET VIANDES:

CREVETTE SAUTE 12.95
BACCALA MARINARA ( MORUES AVEC SAUCE TOMATE) 17.95
BACCALA FRITTO CON CIPOLLA (MORUES AVEC OGNONS FRITS) 13.95
COQUILLE FRUITS DE MER 6.50
PIATTO PREFERITTO DELLE NONNO ( MOULES,CREVETTES ET PALOURDE DANS UNE SAUCE TOMATE) 29.95
COZZE MARINARA ( MOULES AVEC SAUCE TOMATES) 25.95

SAUCISSE MAISON 700G 14.95
SAUCISSE MAISON RAPINI 700G 14.95
POLLO ALLA PARMIGIANA 11.95
COTE LEVEE BBQ 17.95
POULET PANÉ 8.50
OSSOBUCO ALLA MILANESE 28.95
SHORT RIB (CÔTE DE BOEUF) 15.95
JARRET D’AGNEAU 14.95
PILONS DE POULET (6) 12.95
AILES DE POULET (12) 15.95
PORCHETTA (1 MORC.) 7.95

SALADE FRAIS (RÉFRIGÉRÉ)

SALADE FRUIT DE MER 14.95
SALADE DE PIEUVRE 16.95
LÉGUMES GRILLES MARINÉS 6.95

SOUPE FAITS MAISON ET CONGELÉ:

SOUPE PASTINA IN BRODO 4.50
SOUPE TORTELLINI IN BRODO 4.50
SOUPE MINESTRONI DELLA CASA 4.50
SOUPE PASTA E FAGIOLI 4.50
BOUILLIONS DE POULET 2.50

LES PÂTES FRAIS FAITES MAISON CONGELÉ:

TORTELLINI (FARCIE À LA VIANDE) 6.95
RAVIOLI ( FARCIE À LA VIANDE) 6.95
MEDAGLIONI (FARCIE RICOTTA) 6.95
MEDAGLIONI (FARCIE VIANDE/RICOTTA) 6.95
GNOCCHI (FARCIE RICOTTA) 6.95
CANNELLONI (FARCIE AVEC VIANDE) 7.99
MANNICOTTI (FARCIE AVRC FROMAGE RICOTTA) 7.99

FETTUCCINI 6.95
CAVATELLI CLASSICO 6.95
FUSILLI CLASSICO 6.95
TROPHIE 6.95
RIGATONI 6.95
PAPPARDELLI 6.95

CATERING/ TRAITEUR 6-8 PERS 18-22 PERS
PASTA

LASAGNA À LA VIANDE $45.00 $75.00
LASAGNA POMODORO $40.00 $70.00
LASAGNA ALLA DORA ( pates alimentaire, sauce tomate, béchamel oeuf, fromage parmigiano, mozzarella,viande en cubes) $50.00 $85.00
LASAGNA GIARDINIERA $45.00 $75.00
CANNELONI DI CARNE ALLA NAPOLITANA (FARCIE AL LA VIANDE) (10 CANNELLONI) 55$ (20 CANNELLONI)$85
MANNICOTTI DI RICOTTA ALLA NAPOLITANA (FRACIE AVEC FROMAGE) (10MANNICOTTI) 55$ ( 20MANNICOTTI) 85$
RAVIOLI NAPOLITANA $45.00 $85.00
TORTELLINI ROSÉE $55.00 $95.00

VIANDE /POISSON/ FRUITS DE MER MIN 15 PERSONNES

COTES DE VEAU BRAISÉ (SHORT RIB)
JARRET D’AGNEAU
POLLO ALLA PARMIGIANA
SALSICCIA RAPINI
SALSICCIA DI CASA
AILES DE POULET
PILONS DE POULET
BACCALA FRITTO
BACCALA MARINARA
COQUILLES FRUIT DE MER
COZZE MARINARA (MOULES AVEC SAUCE TOMATES)
PIATTO PREFERITTO DEL NONNO (MOULES, PALOURDES ET CREVETTES AVEC SAUCE TOMATES)

SOUPES: 6 PERSONNES 12 PERSONNES
TORTELLINI IN BRODO $30.00 $60.00
MINESTRONE $16.00 $32.00
PASTINA IN BRODO $25.00 $50.00

ANTIPASTO 6/8 PERSONNES 18/22 PERSONNES
SALADE FRUITS DE MER
LÉGUMES GRILLES $50.00 $85.00
ARANCINI ( 12 ARANCINI) 35$ (24 ARANCINI) 70$
POLPETTE DELLA NONNA (boulettes de viandes) (12 BOULETTES) 18$ (24 BOULETTES) 36$
CREVETTES SAUTÉES (30 CREVETTES) 45$ (60 CREVETTES) 85$
MELANZANA ALLA PARMIGIANA (aubergines) $55.00 $95.00

Target Market(s)

all ages

Industry/Entity Type

Grocery Store

Font styles to use
Sans Serif

Colors
fffefc
ec1f27

Requirements
Must have
• must be in French and English must have my logo address and phone number. address : 4170 Boul. Vermandois, Brossard,QC. J4Y 2K8
• Phone number: 450-613-7095
• must be a menu type pamphlet
• add the Facebook and instagram sign
Nice to have
• homemade frozen and sealed to perfection
• Fait Maison, congelé et scellé à la perfection

```html
<!DOCTYPE html>
<html lang="fr">
<head>
<meta charset="utf-8">
<title>Les Aliments De Rossoli – Menu</title>
<link href="https://fonts.googleapis.com/css2?family=Arimo:ital,wght@0,400;0,700;1,400&family=Roboto+Condensed:wght@500;600&family=Great+Vibes&display=swap" rel="stylesheet">
<style>
  :root{
    --red:#e0232b;
    --red-panel:#dc2128;
    --ink:#1d1d1d;
    --paper:#f6f5f3;
    --canvas:#ffffff;
    --white:#fffefc;
    --row:21.8px;
  }
  *{margin:0;padding:0;box-sizing:border-box}
  html,body{width:1200px;height:1000px;overflow:hidden;background:var(--canvas)}
  body{position:relative;font-family:"Arimo",Arial,sans-serif;color:var(--ink)}
  .pamphlet{position:absolute;left:27px;top:85px;width:1148px;height:810px;background:var(--paper);box-shadow:0 6px 14px rgba(0,0,0,.18)}
  .photo{position:absolute}
  .photo--pizza{left:0;top:23px;width:108px;height:344px;background:linear-gradient(90deg,#8a5a32 0%,#c9803e 35%,#d25a2e 70%,#b9442a 100%);border-radius:0 60px 60px 0/0 172px 172px 0}
  .photo--lasagna{left:263px;top:385px;width:120px;height:127px;background:radial-gradient(ellipse at 45% 50%,#e6b35a 0%,#c98a3a 55%,#7d4a26 100%)}
  .photo--veggies{left:383px;top:3px;width:380px;height:147px;background:linear-gradient(100deg,#e9d23c 0%,#c8321f 30%,#6b8a2e 55%,#d93a23 75%,#e9e4dc 100%)}
  .photo--soup{left:670px;top:308px;width:93px;height:164px;background:radial-gradient(circle at 70% 50%,#e8a447 0%,#f3e6c6 35%,#ffffff 55%,#a3774d 100%)}

  .section{position:absolute}
  .heading{font-family:"Roboto Condensed",Arial Narrow,sans-serif;font-weight:600;font-size:17px;color:var(--red);text-transform:uppercase;line-height:22px;letter-spacing:.1px;white-space:nowrap}
  .menu{list-style:none;font-size:13.5px}
  .menu li{display:flex;justify-content:space-between;align-items:flex-start;line-height:var(--row);white-space:nowrap}
  .menu .name{display:block}
  .menu .note{font-style:italic}
  .menu .sub{display:block;font-style:italic;line-height:16.1px;margin-top:-3px;margin-bottom:3px}
  .menu .gap{height:12px}

  .specialty-title{position:absolute;left:25px;top:515px;width:330px;height:70px}
  .specialty-title .rule{position:absolute;top:37px;height:1.5px;background:var(--red)}
  .specialty-title .script{position:absolute;left:86px;top:4px;font-family:"Great Vibes",cursive;font-size:47px;color:var(--red);line-height:50px;white-space:nowrap}
  .specialty-title .sub-title{position:absolute;left:110px;top:55px;font-family:"Arimo",Arial,sans-serif;font-size:15px;color:var(--red);font-weight:700;white-space:nowrap}

  .panel{position:absolute;left:765px;top:0;width:383px;height:810px;background:var(--red-panel);color:var(--white)}
  .panel .heading{color:var(--white);font-size:17.5px}
  .panel .menu{color:var(--white)}
  .contact{position:absolute;left:39px;top:696px;width:311px;height:76px;border:1.5px solid var(--white);border-radius:9px;text-align:center;color:var(--white)}
  .contact .phone{display:flex;align-items:center;justify-content:center;gap:6px;margin-top:6px;font-family:"Arimo",Arial,sans-serif;font-weight:700;font-size:31px;line-height:36px}
  .contact .phone svg{width:26px;height:28px}
  .contact .web{font-size:19px;font-weight:700;letter-spacing:.6px;line-height:22px;margin-top:4px}
</style>
</head>
<body>
<main class="pamphlet">

  <div class="photo photo--pizza" role="img" aria-label="Photo d'une pizza au pepperoni"></div>
  <div class="photo photo--lasagna" role="img" aria-label="Photo d'une lasagne gratinée en barquette"></div>
  <div class="photo photo--veggies" role="img" aria-label="Photo de légumes grillés et marinés"></div>
  <div class="photo photo--soup" role="img" aria-label="Photo d'un bol de soupe maison"></div>

  <section class="section" style="left:114px;top:22px;width:239px">
    <h2 class="heading" style="margin-bottom:2px">Pizza,Calzone Congelé</h2>
    <ul class="menu">
      <li><span class="name">Pizza Napoletana</span><span>9.95</span></li>
      <li><span class="name">Pizza Americana</span><span>12.95</span></li>
      <li><span class="name">Pizza Canadese</span><span>14.95</span></li>
      <li><span class="name">Pizza Spécial De Rossoli</span><span>15.95</span></li>
      <li><span class="name">Pizza Vegeteriana</span><span>10.95</span></li>
      <li><span class="name">Pizza légumes Mix</span><span>13.95</span></li>
      <li><span class="name">Pizza Campagnola</span><span>14.95</span></li>
      <li><span class="name">Pizza Salsiccia e Rapini</span><span>13.50</span></li>
      <li><span class="name">Pizza Bacon</span><span>13.95</span></li>
      <li><span class="name">Pizza Salsiccia di casa</span><span>13.95</span></li>
      <li><span class="name">Pizza Fruits de Mer</span><span>17.95</span></li>
      <li><span class="name">Calzone pepperoni fromage</span><span>6.95</span></li>
      <li><span class="name">Calzone Salsiccia Rapini</span><span>6.95</span></li>
      <li><span class="name">Foccacia All'Alio</span><span>7.95</span></li>
      <li><span class="name">Pâte à Pizza</span><span>1.95</span></li>
    </ul>
  </section>

  <section class="section" style="left:21px;top:392px;width:239px">
    <h2 class="heading" style="margin-bottom:8px">Lasagne Congelé</h2>
    <ul class="menu">
      <li><span class="name">Lasagna Pomodoro</span><span>12.95</span></li>
      <li><span class="name">Lasagna Alla Dora</span><span>14.50</span></li>
      <li><span class="name">Lasagna Sauce Viande</span><span>14.50</span></li>
      <li><span class="name">Lasagna Giardinera</span><span>13.95</span></li>
    </ul>
  </section>

  <div class="specialty-title">
    <span class="rule" style="left:0;width:81px"></span>
    <span class="rule" style="left:248px;width:80px"></span>
    <span class="script">Spécialité</span>
    <span class="sub-title">de la maison De Rossoli</span>
  </div>
  <section class="section" style="left:26px;top:595px;width:328px">
    <ul class="menu">
      <li><span class="name">Arancini (4)</span><span>11.50</span></li>
      <li><span class="name">Polpette Della Nonna (8)</span><span>11.95</span></li>
      <li><span class="name">Melanzane Alla Parmigiana</span><span>15.95</span></li>
      <li><span class="name">Pepperoni Ripieni Di Mamma Lucia</span><span>15.95</span></li>
      <li><span class="name">Cannelloni Al Forno</span><span>15.95</span></li>
      <li><span class="name">Mannicotti Alla Fiorentina</span><span>15.95</span></li>
      <li><span class="name">Polenta Salsiccia</span><span>15.95</span></li>
      <li><span class="name">Trippa</span><span>13.95</span></li>
      <li><span class="name">Pâté Chinois</span><span>16.95</span></li>
    </ul>
  </section>

  <section class="section" style="left:409px;top:167px;width:328px">
    <h2 class="heading" style="text-align:center;margin-bottom:6px">Salade Frais (Réfrigéré)</h2>
    <ul class="menu">
      <li><span class="name">Salade Fruits De Mer</span><span>14.95</span></li>
      <li><span class="name">Salade De Pieuvre</span><span>16.95</span></li>
      <li><span class="name">Légumes Grillés et Marinés</span><span>6.95</span></li>
      <li><span class="name">Peperoncini Piccante</span><span>7.95</span></li>
      <li><span class="name">Champignons Marinés</span><span>7.95</span></li>
    </ul>
  </section>

  <section class="section" style="left:410px;top:321px;width:300px">
    <h2 class="heading" style="margin-bottom:9px">Soupe Faits Maison et Congelé</h2>
    <ul class="menu" style="width:243px">
      <li><span class="name">Soupe Pastina in Brodo</span><span>4.50</span></li>
      <li><span class="name">Soupe Tortellini in Brodo</span><span>4.50</span></li>
      <li><span class="name">Soupe Minestrone Della Casa</span><span>4.50</span></li>
      <li><span class="name">Soupe Pasta e Fagioli</span><span>4.50</span></li>
      <li><span class="name">Bouillon de Poulet</span><span>2.50</span></li>
    </ul>
  </section>

  <section class="section" style="left:409px;top:483px;width:328px">
    <h2 class="heading" style="margin-bottom:8px">Les Pâtes Frais Faites Maison Congelé</h2>
    <ul class="menu">
      <li><span class="name">Tortellini <span class="note">(Farcie Avec Viande)</span></span><span>6.95</span></li>
      <li><span class="name">Ravioli <span class="note">(Farcie Avec Fromage)</span></span><span>6.95</span></li>
      <li><span class="name">Ravioli <span class="note">(Farcie Avec Viande)</span></span><span>6.95</span></li>
      <li><span class="name">Medaglioni <span class="note">(Farcie Viande/Ricotta)</span></span><span>6.95</span></li>
      <li><span class="name">Gnocchi <span class="note">(Farcie Ricotta)</span></span><span>6.95</span></li>
      <li><span class="name">Gnocchi Di Patate</span><span>6.95</span></li>
      <li><span class="name">Cannelloni <span class="note">(Farcie Avec Viande)</span></span><span>7.99</span></li>
      <li><span class="name">Mannicotti <span class="note">(Farcie Avec Fromage Ricotta)</span></span><span>7.99</span></li>
      <li><span class="name">Fettucini</span><span>6.95</span></li>
      <li><span class="name">Cavatelli Classico</span><span>6.95</span></li>
      <li><span class="name">Fusilli Classico</span><span>6.95</span></li>
      <li><span class="name">Trophie</span><span>6.95</span></li>
      <li><span class="name">Rigatoni</span><span>6.95</span></li>
    </ul>
  </section>

  <aside class="panel">
    <section class="section" style="left:34px;top:30px;width:319px">
      <h2 class="heading" style="margin-bottom:7px">Sauces Maison Congelé et Réfrigéré</h2>
      <ul class="menu">
        <li><span class="name">1L Sauce Viande <span class="note">(Réfrigéré)</span></span><span>13.95</span></li>
        <li><span class="name">1L Sauce Napoletana <span class="note">(Réfrigéré)</span></span><span>10.50</span></li>
        <li><span class="name">500ML Sauce Viande Congelé</span><span>6.25</span></li>
        <li><span class="name">500ML Sauce Lina Congelé</span><span>7.95</span></li>
        <li><span class="name">500ML Sauce Serena Congelé <span class="note">(Sauce Rosée)</span></span><span>6.95</span></li>
        <li><span class="name">500ML Sauce Arrabiatta Congelé</span><span>6.95</span></li>
      </ul>
    </section>

    <section class="section" style="left:35px;top:207px;width:318px">
      <h2 class="heading" style="margin-bottom:7px">Poissons, Fruits de Mer et Viandes</h2>
      <ul class="menu">
        <li><span class="name">Crevettes Sautées</span><span>12.95</span></li>
        <li><span class="name">Baccala Marinara<span class="sub">(Morue Avec Sauce Tomate)</span></span><span>17.95</span></li>
        <li><span class="name">Coquille Fruits De Mer</span><span>6.50</span></li>
        <li><span class="name">Piatto Preferitto Delle Nonno<span class="sub">(Moules, Crevettes, et Palourde<br>Dans Une Sauce Tomate)</span></span><span>29.95</span></li>
        <li><span class="name">Cozze Marinara<span class="sub">(Moules Avec Sauce Tomates)</span></span><span>25.95</span></li>
        <li><span class="name">Croquette De Morue <span class="note">(Baccala)</span></span><span>12.95</span></li>
        <li class="gap"></li>
        <li><span class="name">Saucisse Maison 700G</span><span>14.95</span></li>
        <li><span class="name">Saucisse Maison Rapini 700G</span><span>14.95</span></li>
        <li><span class="name">Pollo Alla Parmigiana</span><span>11.95</span></li>
        <li><span class="name">Cote Levee BBQ</span><span>17.95</span></li>
        <li><span class="name">Poulet Pané</span><span>8.50</span></li>
        <li><span class="name">Ossobuco Alla Milanese</span><span>28.95</span></li>
        <li><span class="name">Short Rib <span class="note">(Côte De Boeuf)</span></span><span>15.95</span></li>
        <li><span class="name">Jarret D'Agneu</span><span>14.95</span></li>
        <li><span class="name">Pilons De Poulet (6)</span><span>12.95</span></li>
        <li><span class="name">Ailes De Poulet (12)</span><span>15.95</span></li>
        <li><span class="name">Porchetta (1 Morc.)</span><span>7.95</span></li>
      </ul>
    </section>

    <div class="contact">
      <div class="phone">
        <svg viewBox="0 0 24 24" aria-hidden="true"><path fill="#fffefc" d="M6.6 2.5c.6-.3 1.3-.1 1.6.5l2 3.6c.3.6.2 1.3-.3 1.7L8.4 9.6c1.1 2.4 3.2 4.5 5.6 5.7l1.3-1.5c.4-.5 1.1-.6 1.700-.3l3.6 2c.6.3.8 1 .5 1.6l-1.2 2.6c-.4.8-1.3 1.3-2.2 1.1C9.9 19.3 4.7 14.1 3.2 6.3c-.2-.9.3-1.8 1.1-2.2z"/></svg>
        <span>450-613-7095</span>
      </div>
      <div class="web">www.alimentsderossoli.ca</div>
    </div>
  </aside>

</main>
</body>
</html>
```